Business Card for Academic Coach

I need a business card designed for me - a private tutor/academic coach.

Glen Mabery
Academic Coach
AB Pellwood University, 1994 Cum Laude
Phone: 404-555-0187
glenrmabery@tutormail-example.com

Subjects
QET and BRT
Math, Physics, Writing

```html
<!DOCTYPE html>
<html lang="en">
<head>
<meta charset="utf-8">
<title>Glen Mabery – Academic Coach Business Card</title>
<link rel="stylesheet" href="https://fonts.googleapis.com/css2?family=Arimo:wght@400;700&display=swap">
<style>
  :root {
    --navy-deep: #08173f;
    --navy-mid: #0b2a5a;
    --navy-right: #0c3a6c;
    --accent-blue: #1ba4ea;
    --arc-blue: #1f70b3;
    --text-white: #ffffff;
    --icon-red: #e8473a;
    --rule-orange: #e0622f;
    --faint-art: rgba(60, 110, 170, 0.22);
  }
  * { margin: 0; padding: 0; box-sizing: border-box; }
  html, body {
    width: 1200px; height: 685px; overflow: hidden;
    background: var(--navy-deep);
  }
  .card {
    position: relative; width: 1200px; height: 685px; overflow: hidden;
    font-family: "Arimo", Arial, sans-serif;
    color: var(--text-white);
    background: linear-gradient(90deg, var(--navy-deep) 0%, var(--navy-mid) 55%, var(--navy-right) 100%);
  }
  .background-art {
    position: absolute; left: 0; top: 0; width: 760px; height: 685px;
    background: radial-gradient(ellipse 340px 300px at 420px 320px, var(--faint-art), transparent 75%);
  }
  .divider-arc { position: absolute; left: 0; top: 0; }
  .contact > * { position: absolute; left: 48px; line-height: 1; white-space: nowrap; }
  .contact__name { top: 166px; font-size: 36px; font-weight: 700; color: var(--accent-blue); }
  .contact__role { top: 212px; font-size: 29px; }
  .contact__degree { top: 251px; font-size: 24px; }
  .contact__line {
    display: flex; align-items: center; gap: 8px;
    font-weight: 700;
  }
  .contact__line--phone { top: 331px; font-size: 33px; }
  .contact__line--email { top: 383px; font-size: 31px; }
  .contact__icon { flex: none; }
  .contact__rule { top: 462px; width: 618px; height: 2px; background: var(--rule-orange); }
  .subjects { top: 480px; font-size: 34px; }
  .subjects__dot { color: var(--accent-blue); padding: 0 6px; }
  .brand-name {
    position: absolute; left: 800px; width: 370px; top: 312px;
    text-align: center;
    font-size: 50px; font-weight: 700; line-height: 1;
    color: var(--accent-blue); white-space: nowrap;
  }
</style>
</head>
<body>
  <main class="card">
    <div class="background-art" role="img" aria-label="Faint graduation cap and rolled diploma illustration"></div>

    <svg class="divider-arc" width="1200" height="685" viewBox="0 0 1200 685" aria-hidden="true">
      <path d="M718 42 Q790 342 718 642 Q782 342 718 42 Z" fill="var(--arc-blue)"/>
    </svg>

    <section class="contact">
      <h1 class="contact__name">Glen Mabery</h1>
      <p class="contact__role">Academic Coach</p>
      <p class="contact__degree">AB Pellwood University, 1994 Cum Laude</p>

      <p class="contact__line contact__line--phone">
        <svg class="contact__icon" width="42" height="42" viewBox="0 0 42 42" aria-hidden="true">
          <circle cx="21" cy="21" r="21" fill="var(--icon-red)"/>
          <path d="M14 10c1.5-.8 2.6 0 3.3 1.3l2 3.6c.6 1.2.3 2.2-.8 3l-1.5 1.1c1.2 2.7 3.4 4.9 6.1 6.1l1.1-1.5c.8-1.1 1.8-1.4 3-.8l3.6 2c1.3.7 2.1 1.8 1.3 3.3-1 2-3 3.3-5.3 2.9C18.9 29.8 12.2 23.1 11.1 15.3 10.7 13 12 11 14 10z" fill="#fff"/>
        </svg>
        404.555.0187
      </p>
      <p class="contact__line contact__line--email">
        <svg class="contact__icon" width="42" height="42" viewBox="0 0 42 42" aria-hidden="true">
          <circle cx="21" cy="21" r="21" fill="var(--icon-red)"/>
          <rect x="10" y="13" width="22" height="16" rx="1.5" fill="#fff"/>
          <path d="M10.5 13.8 21 22l10.5-8.2" fill="none" stroke="var(--icon-red)" stroke-width="2"/>
        </svg>
        glenrmabery@tutormail-example.com
      </p>

      <div class="contact__rule"></div>

      <p class="subjects">QET<span class="subjects__dot">•</span>BRT<span class="subjects__dot">•</span>Math<span class="subjects__dot">•</span>Physics<span class="subjects__dot">•</span>Writing</p>
    </section>

    <p class="brand-name">Glen Mabery</p>
  </main>
</body>
</html>
```